Lost & Found Website - PAYMENT GUARANTY

PC website and Mobile Website

Our website aims to develop an online management platform for lost & found objects with the use of stickers.
This solution allows users to buy stickers which will be affixed on the owners’ objects (glasses, laptops, phones …).
Users shall register the code on the website or the mobile application (flashing QR code). Platform will alert by email users if its object is found.
The person who finds an object with a sticker will be encouraged to declare the code on the web/mobile site. Once the object is found, it is identified by the system and the platform notifies the owner via email and give access to contact details of the person who found the object.

PLEASE SEE REQUIREMENT ATTACHED
Updates

Project Deadline Extended
Reason: We are waiting for more interesting ideas. Thank you all for your work. R. Delorme

Project Deadline Extended
Reason: Your designs are very next to perfection !

Target Market(s)

Our target are people 20 to 35 years old who care about there objects. Mainly French market at the beginning.

Industry/Entity Type

Management

Requirements
Must have
• Specifications:

The design must follow basic web design rules:
- Consistent site header/logo
- Page footer area includes copyright, last update, contact e-mail address
- Color scheme is limited to a maximum of three or four colors plus neutrals
- Color is used consistently
- Common fonts such as Arial or Times New Roman are used
- No more than one web font is used
- Fonts, font sizes, and font colors are consistently used
- Information is easy to find (minimal clicks)
- Find a suitable place to put the sponsor's logos.

For mobile version, we need a design that can fit to any screen size,
so please create standard mobile design.
Nice to have
• The website should allow users to:
- Create an account
- Buy lots of stickers
- Associate stickers to their objects
- Report the loss of an object by email
- Access full contact information of the finder after he paid the service
- Declare a found object
- The payment process management via Paytrov platform
Should not have
• Only PSD files.

No html.

```html
<!DOCTYPE html>
<html lang="fr">
<head>
<meta charset="utf-8">
<title>Trouvio – Lost &amp; Found</title>
<link href="https://fonts.googleapis.com/css2?family=Ubuntu:ital,wght@0,300;0,400;0,500;0,700;1,400&display=swap" rel="stylesheet">
<style>
:root{
  --orange:#f05a28;
  --orange-dark:#d94a1c;
  --ink:#333;
  --muted:#999;
  --line:#e2e2e2;
  --white:#fff;
  --dark:#2e2e2e;
  --darker:#3a3a3a;
  --link:#2a9fd6;
  --divider:#c7c3ea;
}
*{box-sizing:border-box;margin:0;padding:0}
html,body{width:758px;height:1200px;overflow:hidden}
body{font-family:'Ubuntu',sans-serif;color:var(--ink);background:#ececec;position:relative;font-size:6.4px;line-height:1.4}
.abs{position:absolute}
.topbar{left:0;top:0;width:758px;height:2px;background:#222}
.buy-tab{left:438px;top:2px;width:58px;height:16px;background:var(--orange);color:#fff;font-size:6px;text-align:center;line-height:16px}
.account-tab{left:496px;top:2px;width:118px;height:16px;background:#333;color:#fff;font-size:6px;line-height:16px;padding-left:20px}
.account-tab span{color:var(--orange)}
.logo{left:142px;top:22px;font-size:30px;font-weight:400;color:#222;display:flex;align-items:center;gap:6px}
.logo i{width:10px;height:10px;border-radius:50%;background:#222;display:block}
.call{left:437px;top:36px;font-size:11px;color:#333}
.call b{color:var(--orange);font-weight:400}
.badge{left:574px;top:24px;width:36px;height:30px;border:1px solid #999;border-radius:50%}
.nav{left:142px;top:66px;width:474px;height:15px;background:var(--white);display:flex;border-bottom:1px solid var(--line)}
.nav a{flex:1;text-align:center;font-size:6px;line-height:15px;color:#333;text-decoration:none;border-right:1px solid var(--line)}
.nav a.on{background:var(--orange);color:#fff;flex:.8}
.hero{left:142px;top:84px;width:474px;height:234px;background:var(--white);box-shadow:0 2px 3px rgba(0,0,0,.1);overflow:hidden}
.step{position:absolute;font-variant:small-caps;font-size:9px;color:#333;text-align:center;letter-spacing:.3px;line-height:1.3}
.step b{color:var(--orange);font-weight:400}
.art{position:absolute;background:linear-gradient(160deg,#f4f4f4,#d9d9d9);border-radius:6px}
.divider{position:absolute;top:0;width:2px;height:234px;background:var(--divider)}
.card{top:336px;width:151px;height:166px;background:var(--white);box-shadow:0 1px 2px rgba(0,0,0,.12);padding:0 5px}
.card h3{font-weight:400;font-size:9.6px;text-align:center;margin:8px 0 6px}
.photo{height:68px;border-radius:1px}
.card p{color:var(--muted);font-size:5.8px;text-align:center;margin:6px 0 5px}
.field{height:15px;background:#eee;border-top:1px solid #ddd;color:#aaa;font-style:italic;font-size:5.6px;line-height:15px;padding-left:6px}
.btn{background:var(--orange);color:#fff;text-align:center;font-weight:500;border-bottom:2px solid var(--orange-dark)}
.card .btn{height:20px;line-height:19px;font-size:9.5px;margin-top:3px}
.quote-band{left:0;top:528px;width:758px;height:96px;background:var(--white);border-top:1px solid var(--line);border-bottom:1px solid var(--line)}
.qmark{position:absolute;font-size:90px;color:#c8c8c8;font-weight:700;line-height:1;font-family:Georgia,serif}
.quote-band h2{position:absolute;left:0;width:758px;top:13px;text-align:center;font-weight:300;font-size:16.5px;color:#222}
.quote-band p{position:absolute;left:144px;width:470px;top:38px;text-align:center;color:#888;font-size:5.8px}
.cite{position:absolute;left:509px;top:62px;font-style:italic;font-size:6.4px;color:#555}
.cite small{display:block;font-size:5.6px;color:#888}
.intro{top:652px;width:235px}
.intro h2{font-weight:400;font-size:12px;color:#333;margin-bottom:4px}
.intro p{color:#888;font-size:6px;margin-bottom:7px}
.box{top:772px;width:111px;height:158px;background:var(--white);box-shadow:0 1px 2px rgba(0,0,0,.12);padding:0 9px}
.box h3{font-weight:400;font-size:9.6px;text-align:center;margin:9px 0 5px}
.box p,.box li{color:#999;font-size:5.6px}
.box .date{color:var(--orange);font-style:italic;font-size:5.2px;margin-bottom:5px}
.box ul{list-style:none}
.box li:before{content:"• ";color:#bbb}
.box .btn{position:absolute;left:5px;right:5px;bottom:13px;height:15px;line-height:14px;font-size:6px;font-weight:400}
.box p.q{margin-bottom:10px}
.qf{height:15px;background:#eee;border-top:1px solid #ccc;color:#aaa;font-style:italic;font-size:5.4px;padding:2px 5px;margin:0 -4px 4px}
.partners{left:0;top:958px;width:758px;height:100px;background:var(--white)}
.partner{position:absolute;top:36px;height:28px;background:#d6d6d6;border-radius:2px}
.footer{left:0;top:1058px;width:758px;height:120px;background:var(--dark)}
.fcol{position:absolute;top:18px;width:112px;color:#888;font-size:5.8px}
.fcol h4{color:#fff;font-size:7.6px;font-weight:500;margin-bottom:8px}
.fcol a{color:var(--link);text-decoration:none;display:block;line-height:1.35}
.fcol .pair{display:flex;gap:18px}
.fcol p{margin-bottom:6px}
.fcol .row{display:flex;gap:4px;margin-bottom:4px}
.fcol .row b{color:#ddd;font-weight:500}
.fcol svg{flex:none}
.sub{display:flex;margin:4px 0 8px}
.sub span{flex:1;height:14px;background:#3a3a3a;font-style:italic;color:#bbb;font-size:5.4px;line-height:14px;padding-left:5px}
.sub em{width:18px;height:14px;background:#444;color:#fff;font-style:normal;text-align:center;line-height:14px}
.social{display:flex;gap:3px}
.social i{width:11px;height:11px;background:#5b7fbf;display:block;border-radius:1px}
.copy{left:0;top:1178px;width:758px;height:22px;background:var(--darker);color:#999;font-size:5.4px;text-align:center;line-height:22px}
</style>
</head>
<body>
<div class="abs topbar"></div>
<div class="abs buy-tab">Buy Stickers</div>
<div class="abs account-tab"><span>Sign Up</span> or <span>Log in</span> &nbsp;&nbsp;&nbsp;Support</div>

<div class="abs logo"><i></i>Trouvio</div>
<div class="abs call"><b>Call Now</b> 1800 555 0199</div>
<div class="abs badge"></div>

<nav class="abs nav">
  <a class="on">Home</a><a>About Us</a><a>How it works</a><a>Buy Stickers</a><a>Report</a><a>Testimonials</a><a>Help</a><a>Contact Us</a>
</nav>

<section class="abs hero">
  <div class="step" style="left:22px;top:26px;width:160px"><b>1.</b> Enregistrez vos codes<br>Trouvio sur www.trouvio.fr</div>
  <div class="art" role="img" aria-label="Figure lying by a laptop with sticker rolls" style="left:20px;top:70px;width:160px;height:120px"></div>
  <div style="position:absolute;left:12px;top:208px;font-size:14px;color:#222">Trouvio</div>
  <div class="divider" style="left:168px;transform:skewX(-16deg)"></div>
  <div class="art" role="img" aria-label="Rolls of code stickers" style="left:215px;top:18px;width:100px;height:62px"></div>
  <div class="step" style="left:196px;top:114px;width:140px;text-align:right"><b>2.</b> Collez vos stickers</div>
  <div class="art" role="img" aria-label="Phone, laptop and wallet with stickers" style="left:190px;top:140px;width:140px;height:82px"></div>
  <div class="divider" style="left:328px;transform:skewX(8deg)"></div>
  <div class="step" style="left:336px;top:16px;width:130px"><b>3.</b> Vous serez contactés si l'un de vos objets est retrouvé</div>
  <div class="art" role="img" aria-label="Figure celebrating by a laptop with phone and email symbol" style="left:352px;top:78px;width:112px;height:144px"></div>
</section>

<article class="abs card" style="left:142px">
  <h3>Found Object ? Declare it</h3>
  <div class="photo" role="img" aria-label="Father and son smiling outdoors" style="background:linear-gradient(135deg,#6f9a3c,#c9a27a)"></div>
  <p>Class aptent taciti sociosqu ad litora torquent per conubia nostra, per inceptos himenaeos.</p>
  <div class="field">Enter Code here</div>
  <div class="btn">Declare Found Object</div>
</article>
<article class="abs card" style="left:303px">
  <h3>Lost Object ?&nbsp; Declare it</h3>
  <div class="photo" role="img" aria-label="Hand dialing a desk telephone" style="background:linear-gradient(135deg,#9aa2a8,#e4e6e8)"></div>
  <p>Class aptent taciti sociosqu ad litora torquent per conubia nostra, per inceptos himenaeos.</p>
  <div class="field">Enter Code here</div>
  <div class="btn">Declare Lost Object</div>
</article>
<article class="abs card" style="left:465px">
  <h3>Register your objects</h3>
  <div class="photo" role="img" aria-label="Smiling young woman in an office" style="background:linear-gradient(135deg,#d8d8d8,#b88a66)"></div>
  <p>Class aptent taciti sociosqu ad litora torquent per conubia nostra, per inceptos himenaeos.</p>
  <div class="field">Enter Code here</div>
  <div class="btn">Register Code</div>
</article>

<section class="abs quote-band">
  <div class="qmark" style="left:86px;top:-8px">&ldquo;</div>
  <div class="qmark" style="left:610px;top:-8px">&rdquo;</div>
  <h2>Best online management platform for lost and found objects</h2>
  <p>Class aptent taciti sociosqu ad litora torquent per conubia nostra, per inceptos himenaeos. Mauris in erat justo. Nullam ac urna eu felis dapibus condimentum sit amet a augue. Sed non neque elit. Sed ut imperdiet nisi. Proin condimentum fermentum nunc. Etiam pharetra, erat sed fermentum feugiat, velit mauris egestas quam, ut aliquam massa nisl quis neque. Suspendisse in orci enim.</p>
  <div class="cite"><b>Marc Olivier</b><small>American Student</small></div>
</section>

<section class="abs intro" style="left:140px">
  <h2>Welcome to Trouvio</h2>
  <p>This is a sample version of Lorem Ipsum. Proin gravida nibh vel velit auctor aliquet. Aenean sollicitudin, lorem quis bibendum auctor, nisi elit consequat ipsum, nec sagittis sem nibh id elit. Duis sed odio sit amet nibh vulputate cursus a sit amet mauris. Morbi accumsan ipsum velit. Nam nec tellus a odio tincidunt auctor a ornare odio. Sed non mauris vitae erat consequat auctor eu in elit.</p>
  <p>Class aptent taciti sociosqu ad litora torquent per conubia nostra, per inceptos himenaeos. Mauris in erat justo.</p>
</section>
<section class="abs intro" style="left:383px">
  <h2>How it works</h2>
  <p>This is a sample version of Lorem Ipsum. Proin gravida nibh vel velit auctor aliquet. Aenean sollicitudin, lorem quis bibendum auctor, nisi elit consequat ipsum, nec sagittis sem nibh id elit. Duis sed odio sit amet nibh vulputate cursus a sit amet mauris.</p>
  <p>Morbi accumsan ipsum velit. Nam nec tellus a odio tincidunt auctor a ornare odio. Sed non mauris vitae erat consequat auctor eu in elit. Class aptent taciti sociosqu ad litora torquent per conubia nostra, per inceptos himenaeos.</p>
</section>

<aside class="abs box" style="left:142px">
  <h3>News &amp; Events</h3>
  <p>Sed ut imperdiet nisi proin condimentum Fermentum nunc.</p><p class="date">April 18, 2013</p>
  <p>Sed ut imperdiet nisi proin condimentum Fermentum nunc.</p><p class="date">April 18, 2013</p>
  <p>Sed ut imperdiet nisi proin condimentum Fermentum nunc proin gravida donouts</p><p class="date">April 18, 2013</p>
  <p>Sed ut imperdiet nisi proin condimentum Fermentum nunc.</p><p class="date">April 18, 2013</p>
</aside>
<aside class="abs box" style="left:263px">
  <h3>Recenty Found</h3>
  <ul>
    <li>Sed ut imperdiet nisi.</li><li>Proin condimentum</li><li>Fermentum nunc.</li><li>Etiam pharetra, erat sed</li><li>Sed ut imperdiet nisi.</li><li>Proin condimentum</li><li>Fermentum nunc.</li><li>Etiam pharetra, erat sed</li><li>Sed ut imperdiet nisi.</li><li>Proin condimentum</li><li>Fermentum nunc.</li><li>Proin condimentum</li>
  </ul>
  <div class="btn">All Found Objects</div>
</aside>
<aside class="abs box" style="left:383px">
  <h3>FAQs</h3>
  <p class="q">Sed ut imperdiet nisi proin condimentum Fermentum nunc proin gravida donouts ?</p>
  <p class="q">Sed ut imperdiet nisi proin condimentum Fermentum nunc proin gravida donouts ?</p>
  <p class="q">Sed ut imperdiet nisi proin condimentum Fermentum nunc proin gravida donouts ?</p>
  <div class="btn">All FAQs</div>
</aside>
<aside class="abs box" style="left:504px">
  <h3>Quick Contact</h3>
  <p style="margin-left:-3px">Get in touch.<br><b style="color:var(--orange);font-weight:500">Call +1 800 555 0142</b></p>
  <div style="height:6px"></div>
  <div class="qf">Name</div>
  <div class="qf">Email Address</div>
  <div class="qf" style="height:52px">Question</div>
  <div class="btn">Declare found object</div>
</aside>

<section class="abs partners" aria-label="Partners">
  <div class="partner" style="left:140px;width:46px;height:40px;top:30px"></div>
  <div class="partner" style="left:212px;width:68px;height:16px;top:42px"></div>
  <div class="partner" style="left:306px;width:46px;top:36px;border-radius:50%"></div>
  <div class="partner" style="left:388px;width:48px;height:34px;top:32px"></div>
  <div class="partner" style="left:470px;width:50px;height:22px;top:40px"></div>
  <div class="partner" style="left:543px;width:70px;height:30px;top:34px"></div>
</section>

<footer class="abs footer">
  <div class="fcol" style="left:142px">
    <h4>Quick Links</h4>
    <div class="pair">
      <div><a>Home</a><a>About Us</a><a>Contact Us</a><a>Terms</a><a>Products</a><a>Downloads</a><a>Aenean</a><a>Sollicitudin</a></div>
      <div><a>Lorem Ipsum</a><a>Proin</a><a>Gravida</a><a>Nibh vel velit</a><a>Auctor aliquet</a></div>
    </div>
  </div>
  <div class="fcol" style="left:262px">
    <h4>Latest Tweets</h4>
    <p>Proin gravida nibh vel velit auctor aliquet. Aenean sollicitudin, lorem <a>http://trouvio.blog/notes</a></p>
    <p>Proin gravida nibh vel velit auctor aliquet. Aenean sollicitudin, lorem <a>http://trouvio.blog/notes</a></p>
  </div>
  <div class="fcol" style="left:383px;width:116px">
    <h4>Contact Details</h4>
    <div class="row"><svg width="7" height="8" viewBox="0 0 7 8"><path d="M3.5 0a3 3 0 0 0-3 3c0 2 3 5 3 5s3-3 3-5a3 3 0 0 0-3-3z" fill="#ddd"/><circle cx="3.5" cy="3" r="1" fill="#2e2e2e"/></svg><span><b>Address:</b> Trouvio gravida nibh vel, 30 Aelit auctor Canada</span></div>
    <div class="row" style="margin-top:6px"><svg width="7" height="7" viewBox="0 0 7 7"><path d="M1 0h1.5l.7 1.8-1 .7a4 4 0 0 0 2.3 2.3l.7-1 1.8.7V7C3 7 0 4 0 1z" fill="#ddd"/></svg><span><b>Phone:</b> +33 555 010 482</span></div>
    <div class="row"><svg width="7" height="7" viewBox="0 0 7 7"><rect x="0" y="2" width="7" height="4" fill="#ddd"/><rect x="1.5" y="0" width="4" height="2" fill="#ddd"/></svg><span><b>Fax:</b> +33 555 010 483</span></div>
    <div class="row"><svg width="7" height="7" viewBox="0 0 7 7"><rect x="0" y="1" width="7" height="5" fill="#ddd"/><path d="M0 1l3.5 3L7 1" stroke="#2e2e2e" fill="none" stroke-width=".7"/></svg><span><b>Email:</b> <a style="display:inline">contact@trouvio-mail.fr</a></span></div>
  </div>
  <div class="fcol" style="left:505px">
    <h4>Subscribe Newsletter</h4>
    <p>Proin gravida nibh vel velit auctor aliquet. Aenean sollicitudin, lorem</p>
    <div class="sub"><span>email address</span><em>Go</em></div>
    <h4 style="margin-bottom:5px">Follow Us</h4>
    <div class="social"><i></i><i></i><i></i><i></i><i style="background:#c43"></i><i style="background:#e2672b"></i></div>
  </div>
</footer>
<div class="abs copy">© Copyright 2013 &nbsp;|&nbsp; All Rights Reserved &nbsp;|&nbsp; Privacy Policy</div>
</body>
</html>
```